Comparison Website Design for Glue Website

Note: We don't have a logo, it's not needed. Just put placeholder.

We would like a website comparing A to B, simple elegant design, simplistic styling. Website is for helping people find the best glue to glue 2 things together. For example, Metal to wood, Metal to rubber, glass to fabric and so on. Select 2 options and be shown the best glue/adhesive for the job.

Purpose of the website:
Allowing someone to pick 2 materials they want to glue together, and showing them the best product for it. We want someone to select 2 materials like "Metal and Rubber". It'll then show the best glues/adhesives from best #1 to #5-10 other ones. The design is simple and doesn't need much detail.

Design rules:
Please design using bootstrap 4 with a modified 1440px width.

We're looking for 4 main pages:
Home Page, Compare Page, Category Page, Product Page.

Target Market(s)

Everyone

Industry/Entity Type

Adhesive

Number of Pages Required

3 page

Font styles to use
Sans Serif

Colors
876aae
b7a5cd
6b449b
e4daeb
fefeff

Requirements
Must have
• We like the following features of these designs:
https://pixlorum.net/works/7310284-Cavrano-Dashboard - Main menu with the drop down, this will change depending on the active page. If they are on a metal page they could be shown "glue metal to ___" options. We also like the simple table view in this design under "users" heading.

https://pixlorum.net/works/7228451-Quotation-Page - The entire colour palette is great! The simplicity of the design is great.

https://pixlorum.net/works/9107642-Comparison-UI - The boxes at the top look great, if there was 2 of these with a compare icon between them and above that saying "glue metal to rubber" and it shows an icon/image or metal and glue... The table of products is also good, it has dot points and details which we like.

https://pixlorum.net/works/5093718-Send-Funds/attachments/5093718-Send-Funds?mode=media - The right it shows which 2 products are selected (metal and rubber) for example, on the left it would say "best glue for metal and rubber". This is too detailed though, so it would need to be simplified nicely.

https://linquora.net/ - They do a good job of "comparing" 2 things and displaying integrations well. You can get lots of ideas from them linking A to B similar to what we want to show.

https://www.flowtoolreviewdesk.net/brivelo-vs-tandrix/ - This shows a good example of the hero section how it should look.

Features of each page to help you design:
Home Page-
Menu (shown in examples above)
Hero section (colour section) with a centre heading saying "what do you want to glue together" with 2 boxes below to select materials from.
List of most popular searches (metal to rubber, glass to wood, fabric to leather... repeat these to fill space).
List of popular products with basic details about each one (grid format, not list).
FAQs - You choose design for this
Content section (simple design, headings, paragraphs, dotpoints, images...)
Blog section - Simple 3 column grid with an image on top, heading, paragraph, button.

Compare Page-
Showing 2 materials in the colour hero section under or to the right of the heading and paragraph.
Best product (highlighted)
9 other products (list table)
3 column section saying glue (product a to ___) with other product that isn't product b + reverse of this.
Content section

Category page-
heading and breadcrumbs in hero section
Standard product list 1 column on the left with filters, 3 products shown on the right in grid format with basic details on each one.

Product page-
Image left, details on the right.
Keep the image smaller not 50% as we want it to not take up too much space vertically.
Under this put a table where this product ranks for gluing things together. for example #3 for gluing metal to rubber, #1 for glass to wood.
Content section.

Please note, keep this design flat, simple and pretty. We don't need it over-designed or detailed, we simply want a simple functionality website that clearly shows what we're looking for.

```html
<!DOCTYPE html>
<html lang="en">
<head>
<meta charset="utf-8">
<title>Glue Compare – Home</title>
<link href="https://fonts.googleapis.com/css2?family=Montserrat:ital,wght@0,400;0,500;0,600;0,700;1,400;1,500&display=swap" rel="stylesheet">
<style>
:root{
  --hero:#7252bc;
  --hero-line:#6a49b3;
  --dark:#2f2a4e;
  --pale:#ebe6fb;
  --panel:#eeebf7;
  --grey-box:#c4c3db;
  --faq:#c3c2d8;
  --btn:#6f4fbd;
  --blog:#7469a8;
  --text:#2c2844;
  --muted:#55516b;
  --white:#fefeff;
  --star:#f5e400;
}
*{box-sizing:border-box;margin:0;padding:0}
html,body{width:1200px;height:2852px;overflow:hidden}
body{font-family:'Montserrat',sans-serif;color:var(--text);background:var(--pale);position:relative}
.abs{position:absolute}
.hero{left:0;top:0;width:1200px;height:437px;background:var(--hero)}
.nav{left:0;top:0;width:1200px;height:63px;border-bottom:1px solid var(--hero-line)}
.brand{left:149px;top:20px;color:var(--white);font-size:20px;font-weight:600}
.nav-links{left:0;top:25px;font-size:11px;font-weight:600;color:var(--white)}
.nav-links span{position:absolute;white-space:nowrap}
.nav-select{display:inline-block;width:34px;border-bottom:1px solid #b7a5cd;margin:0 4px;position:relative;top:-2px}
.hero-title{left:0;width:1200px;top:118px;text-align:center;color:var(--white);font-size:31px;font-weight:500}
.mat-box{top:176px;width:136px;height:132px;border-radius:3px}
.mat-box.chosen{left:433px;background:var(--dark)}
.mat-box.empty{left:631px;background:var(--grey-box)}
.mat-box .label{position:absolute;left:0;right:0;top:88px;border-top:1px solid var(--hero);height:44px;line-height:44px;font-size:11px;color:var(--white);text-align:center}
.mat-box.empty .label{color:#8f8aa8;font-style:italic;text-align:left;padding-left:13px}
.mat-box .q{position:absolute;top:24px;width:100%;text-align:center;font-size:28px;color:#8f8aa8}
.hero-to{left:588px;top:228px;color:var(--white);font-size:20px;font-weight:600}
.btn{display:block;text-align:center;font-size:12px;font-weight:600;border-radius:2px}
.btn-white{background:var(--white);color:var(--btn)}
.btn-purple{background:var(--btn);color:var(--white)}
.btn-outline{border:2px solid var(--btn);color:var(--btn);background:var(--white)}
.sec-title{left:0;width:1200px;text-align:center;font-size:23px;font-weight:600;color:var(--text)}
.search-row{left:218px;width:764px;height:105px;background:var(--white);border-radius:3px;box-shadow:0 2px 6px rgba(80,60,140,.08)}
.search-row .pair{position:absolute;left:0;width:199px;height:105px;border-right:1px solid #e4daeb}
.search-row .pair .m{position:absolute;top:22px;width:60px;text-align:center;font-size:11px;font-weight:600}
.search-row .pair .m svg{display:block;margin:0 auto 2px}
.search-row .pair .to{position:absolute;left:98px;top:38px;font-size:11px;font-weight:600}
.search-row .pair .views{position:absolute;top:81px;width:199px;text-align:center;font-size:7px;color:var(--btn)}
.glue-list{position:absolute;left:230px;top:18px;list-style:none;font-size:10.5px;color:var(--muted)}
.glue-list li{height:19.5px;display:flex;align-items:center;gap:10px}
.view-all{position:absolute;left:230px;top:83px;font-size:8px;font-style:italic;color:var(--btn)}
.search-row .side{position:absolute;left:565px;top:0;width:199px;height:105px;background:var(--panel);border-radius:0 3px 3px 0}
.search-row .side .btn{position:absolute;left:37px;top:34px;width:124px;height:37px;line-height:37px}
.pager{left:553px;top:915px;display:flex;align-items:center;gap:6px;font-size:12px;font-weight:700;color:var(--btn)}
.pager .pg{width:18px;height:18px;border:1px solid #7a7690;border-radius:3px;display:flex;align-items:center;justify-content:center}
.pager .pg.on{background:var(--dark);border-color:var(--dark)}
.product{top:1048px;width:211px;height:262px;background:var(--white);border-radius:3px;box-shadow:0 2px 6px rgba(80,60,140,.08);overflow:hidden}
.product .img{height:134px;background:linear-gradient(160deg,#d2d0d5,#bdbbc1);position:relative}
.product .stars{position:absolute;left:12px;bottom:8px;color:var(--star);font-size:12px;letter-spacing:1px}
.product h3{font-size:15.5px;font-weight:500;margin:12px 0 8px 12px;white-space:nowrap}
.product p{font-size:10px;color:var(--muted);margin:0 0 8px 12px}
.product p b{font-weight:600;color:var(--text)}
.more{font-size:10.5px;font-style:italic;font-weight:500;color:var(--btn);display:flex;align-items:center;gap:6px}
.product .more{margin-left:12px}
.dots{left:581px;top:1341px;display:flex;gap:8px}
.dots i{width:7px;height:7px;border-radius:50%;background:#a394cf}
.dots i.on{background:var(--btn)}
.faq{left:218px;width:764px;height:53px;background:var(--faq);border-radius:3px;font-size:11.5px;color:var(--text);display:flex;align-items:center}
.faq svg{margin:0 26px 0 24px}
.blog{left:0;top:1913px;width:1200px;height:596px;background:var(--blog)}
.blog-card{top:2024px;width:287px;height:359px;background:var(--white);border-radius:3px;overflow:hidden}
.blog-card .img{height:190px}
.blog-card h3{font-size:15.5px;font-weight:500;margin:16px 18px 10px}
.blog-card p{font-size:12px;line-height:17px;color:var(--muted);margin:0 18px 14px}
.blog-card .more{margin-left:18px}
.footer{left:0;top:2509px;width:1200px;height:343px;background:var(--pale)}
.f-logo{left:0;width:1200px;top:2563px;text-align:center;font-size:23px;font-weight:600}
.f-head{top:2614px;font-size:16px;font-weight:500}
.f-list{top:2648px;list-style:none;font-size:10px;color:var(--muted)}
.f-list li{height:19px}
.f-select{left:149px;width:137px;height:30px;background:var(--faq);border-radius:3px;font-size:10px;font-style:italic;color:#77728f;display:flex;align-items:center;justify-content:space-between;padding:0 12px}
.f-line{left:149px;top:2812px;width:901px;border-top:1px solid #8f85bd}
.social{left:149px;top:2821px;display:flex;gap:11px}
.social i{width:18px;height:18px;border-radius:50%;background:var(--dark)}
.legal{top:2827px;font-size:8px;color:var(--muted)}
</style>
</head>
<body>

<div class="abs hero"></div>
<div class="abs nav"></div>
<div class="abs brand">Logo</div>
<div class="abs nav-links">
  <span style="left:700px">Compare</span>
  <span style="left:779px">Category</span>
  <span style="left:858px">Products</span>
  <span style="left:937px">Glue <i class="nav-select"></i> to <i class="nav-select"></i></span>
</div>

<h1 class="abs hero-title">What do you want to glue together</h1>
<div class="abs mat-box chosen">
  <svg width="62" height="40" viewBox="0 0 62 40" style="position:absolute;left:37px;top:24px" fill="none" stroke="#fefeff" stroke-width="2.4">
    <rect x="10" y="2" width="48" height="12" rx="6"/><rect x="4" y="14" width="52" height="12" rx="6"/><rect x="10" y="26" width="48" height="12" rx="6"/>
    <circle cx="10" cy="20" r="5"/><circle cx="16" cy="8" r="5"/><circle cx="16" cy="32" r="5"/>
  </svg>
  <div class="label">Wood</div>
</div>
<div class="abs hero-to">to</div>
<div class="abs mat-box empty">
  <div class="q">?</div>
  <div class="label">Select
    <svg width="14" height="8" viewBox="0 0 14 8" style="position:absolute;right:12px;top:18px" fill="none" stroke="#6d6888" stroke-width="1.4"><path d="M1 1l6 6 6-6"/></svg>
  </div>
</div>
<a class="abs btn btn-white" style="left:506px;top:338px;width:188px;height:37px;line-height:37px">Compare</a>

<h2 class="abs sec-title" style="top:494px">Popular Searches</h2>

<div class="abs search-row" style="top:548px">
  <div class="pair">
    <div class="m" style="left:24px"><svg width="52" height="30" viewBox="0 0 62 40" fill="none" stroke="#2f2a4e" stroke-width="2.4"><rect x="10" y="2" width="48" height="12" rx="6"/><rect x="4" y="14" width="52" height="12" rx="6"/><rect x="10" y="26" width="48" height="12" rx="6"/><circle cx="10" cy="20" r="5"/><circle cx="16" cy="8" r="5"/><circle cx="16" cy="32" r="5"/></svg>Wood</div>
    <div class="to">to</div>
    <div class="m" style="left:129px"><svg width="34" height="32" viewBox="0 0 34 32" fill="none" stroke="#2f2a4e" stroke-width="1.6"><rect x="5" y="3" width="24" height="26"/><path d="M10 12l6-6M12 20l10-10"/></svg>Glass</div>
    <div class="views">12,345 views</div>
  </div>
  <ul class="glue-list"><li><svg width="11" height="9"><path d="M1 5l3 3 6-7" fill="none" stroke="#6f4fbd" stroke-width="2"/></svg>Bondra : Super wood glue</li><li><svg width="11" height="9"><path d="M1 5l3 3 6-7" fill="none" stroke="#6f4fbd" stroke-width="2"/></svg>Bondra : Super wood glue</li><li><svg width="11" height="9"><path d="M1 5l3 3 6-7" fill="none" stroke="#6f4fbd" stroke-width="2"/></svg>Bondra : Super wood glue</li></ul>
  <div class="view-all">View all &nbsp;⟶</div>
  <div class="side"><a class="btn btn-purple">Compare Now</a></div>
</div>

<div class="abs search-row" style="top:666px">
  <div class="pair">
    <div class="m" style="left:24px"><svg width="34" height="32" viewBox="0 0 34 32" fill="none" stroke="#2f2a4e" stroke-width="1.6"><rect x="8" y="2" width="12" height="26" rx="2"/><path d="M20 8h6v20H8"/></svg>Fabric</div>
    <div class="to">to</div>
    <div class="m" style="left:129px"><svg width="34" height="32" viewBox="0 0 34 32" fill="none" stroke="#2f2a4e" stroke-width="1.6"><path d="M9 3l4 3h8l4-3 3 6-3 4v10l3 4-3 3h-16l-3-3 3-4V13l-3-4z"/></svg>Leather</div>
    <div class="views">10,565 views</div>
  </div>
  <ul class="glue-list"><li><svg width="11" height="9"><path d="M1 5l3 3 6-7" fill="none" stroke="#6f4fbd" stroke-width="2"/></svg>Bondra : Super wood glue</li><li><svg width="11" height="9"><path d="M1 5l3 3 6-7" fill="none" stroke="#6f4fbd" stroke-width="2"/></svg>Bondra : Super wood glue</li><li><svg width="11" height="9"><path d="M1 5l3 3 6-7" fill="none" stroke="#6f4fbd" stroke-width="2"/></svg>Bondra : Super wood glue</li></ul>
  <div class="view-all">View all &nbsp;⟶</div>
  <div class="side"><a class="btn btn-purple">Compare Now</a></div>
</div>

<div class="abs search-row" style="top:784px">
  <div class="pair">
    <div class="m" style="left:24px"><svg width="52" height="30" viewBox="0 0 62 40" fill="none" stroke="#2f2a4e" stroke-width="2.4"><rect x="10" y="2" width="48" height="12" rx="6"/><rect x="4" y="14" width="52" height="12" rx="6"/><rect x="10" y="26" width="48" height="12" rx="6"/><circle cx="10" cy="20" r="5"/><circle cx="16" cy="8" r="5"/><circle cx="16" cy="32" r="5"/></svg>Wood</div>
    <div class="to">to</div>
    <div class="m" style="left:129px"><svg width="34" height="32" viewBox="0 0 34 32" fill="none" stroke="#2f2a4e" stroke-width="1.6"><path d="M4 16l10-12h16L20 16zM4 16h16v12H4zM20 16l10-12v12L20 28"/></svg>Metal</div>
    <div class="views">8,678 views</div>
  </div>
  <ul class="glue-list"><li><svg width="11" height="9"><path d="M1 5l3 3 6-7" fill="none" stroke="#6f4fbd" stroke-width="2"/></svg>Bondra : Super wood glue</li><li><svg width="11" height="9"><path d="M1 5l3 3 6-7" fill="none" stroke="#6f4fbd" stroke-width="2"/></svg>Bondra : Super wood glue</li><li><svg width="11" height="9"><path d="M1 5l3 3 6-7" fill="none" stroke="#6f4fbd" stroke-width="2"/></svg>Bondra : Super wood glue</li></ul>
  <div class="view-all">View all &nbsp;⟶</div>
  <div class="side"><a class="btn btn-purple">Compare Now</a></div>
</div>

<div class="abs pager">
  <span class="pg"><svg width="8" height="10"><path d="M6 1L2 5l4 4" fill="none" stroke="#2f2a4e" stroke-width="1.3"/></svg></span>
  <span style="color:#2f2a4e">1</span><span>2</span><span>3</span><span>4</span>
  <span class="pg on"><svg width="8" height="10"><path d="M2 1l4 4-4 4" fill="none" stroke="#fefeff" stroke-width="1.3"/></svg></span>
</div>

<h2 class="abs sec-title" style="top:990px">Popular Products</h2>
<svg class="abs" style="left:104px;top:1166px" width="16" height="28"><path d="M14 2L2 14l12 12" fill="none" stroke="#2f2a4e" stroke-width="1.6"/></svg>
<svg class="abs" style="left:1080px;top:1166px" width="16" height="28"><path d="M2 2l12 12L2 26" fill="none" stroke="#2f2a4e" stroke-width="1.6"/></svg>

<div class="abs product" style="left:149px">
  <div class="img" role="img" aria-label="Product photo of a glue stick"><span class="stars">★★★★★</span></div>
  <h3>Tackwell's PRIME glue</h3>
  <p><b>Brand</b> : Tackwell</p><p><b>Gun Type</b> : Hobby &amp; Craft</p><p><b>Bonds To</b> : Paper , Wood</p>
  <span class="more">Learn More <svg width="22" height="6"><path d="M0 3h20M16 0l4 3-4 3" fill="none" stroke="#6f4fbd"/></svg></span>
</div>
<div class="abs product" style="left:380px">
  <div class="img" role="img" aria-label="Product photo of a yellow glue stick"><span class="stars">★★★★★</span></div>
  <h3>Tackwell's PRIME glue</h3>
  <p><b>Brand</b> : Tackwell</p><p><b>Gun Type</b> : Hobby &amp; Craft</p><p><b>Bonds To</b> : Paper , Wood</p>
  <span class="more">Learn More <svg width="22" height="6"><path d="M0 3h20M16 0l4 3-4 3" fill="none" stroke="#6f4fbd"/></svg></span>
</div>
<div class="abs product" style="left:609px">
  <div class="img" role="img" aria-label="Product photo of a liquid glue bottle"><span class="stars">★★★★★</span></div>
  <h3>Tackwell's PRIME glue</h3>
  <p><b>Brand</b> : Tackwell</p><p><b>Gun Type</b> : Hobby &amp; Craft</p><p><b>Bonds To</b> : Paper , Wood</p>
  <span class="more">Learn More <svg width="22" height="6"><path d="M0 3h20M16 0l4 3-4 3" fill="none" stroke="#6f4fbd"/></svg></span>
</div>
<div class="abs product" style="left:839px">
  <div class="img" role="img" aria-label="Product photo of a glue tube"><span class="stars">★★★★★</span></div>
  <h3>Tackwell's PRIME glue</h3>
  <p><b>Brand</b> : Tackwell</p><p><b>Gun Type</b> : Hobby &amp; Craft</p><p><b>Bonds To</b> : Paper , Wood</p>
  <span class="more">Learn More <svg width="22" height="6"><path d="M0 3h20M16 0l4 3-4 3" fill="none" stroke="#6f4fbd"/></svg></span>
</div>
<div class="abs dots"><i class="on"></i><i></i><i></i></div>
<a class="abs btn btn-purple" style="left:506px;top:1379px;width:188px;height:38px;line-height:38px">View All Products</a>

<h2 class="abs sec-title" style="top:1475px">Frequently Asked Questions</h2>
<div class="abs faq" style="top:1529px"><svg width="12" height="7"><path d="M1 1l5 5 5-5" fill="none" stroke="#2f2a4e" stroke-width="1.2"/></svg>How to compare between two products ?</div>
<div class="abs faq" style="top:1595px"><svg width="12" height="7"><path d="M1 1l5 5 5-5" fill="none" stroke="#2f2a4e" stroke-width="1.2"/></svg>How to compare between two products ?</div>
<div class="abs faq" style="top:1662px"><svg width="12" height="7"><path d="M1 1l5 5 5-5" fill="none" stroke="#2f2a4e" stroke-width="1.2"/></svg>How to compare between two products ?</div>
<div class="abs faq" style="top:1728px"><svg width="12" height="7"><path d="M1 1l5 5 5-5" fill="none" stroke="#2f2a4e" stroke-width="1.2"/></svg>How to compare between two products ?</div>
<a class="abs btn btn-outline" style="left:506px;top:1812px;width:188px;height:38px;line-height:34px">View All Help Articles</a>

<div class="abs blog"></div>
<h2 class="abs sec-title" style="top:1969px;color:var(--white)">Blog Articles</h2>
<div class="abs blog-card" style="left:149px">
  <div class="img" role="img" aria-label="Photo of hands gluing paper craft pieces on a wooden table" style="background:linear-gradient(135deg,#5a3a2a,#3f6f86 60%,#6b4a36)"></div>
  <h3>Best ways to use glue in craft</h3>
  <p>Lorem ipsum dolor sit amet, consectetur adipisicing elit, sed do eiusmod tempor incididunt ut labore et dolore magna aliqua. Ut enim ad minim veniam, quis nostrud exercitation ut.</p>
  <span class="more">Learn More <svg width="22" height="6"><path d="M0 3h20M16 0l4 3-4 3" fill="none" stroke="#6f4fbd"/></svg></span>
</div>
<div class="abs blog-card" style="left:456px">
  <div class="img" role="img" aria-label="Photo of gloved hands applying glue from a tube" style="background:linear-gradient(135deg,#4b3f7a,#d8d6e4 55%,#2d2b45)"></div>
  <h3>How to safely use glue in art</h3>
  <p>Lorem ipsum dolor sit amet, consectetur adipisicing elit, sed do eiusmod tempor incididunt ut labore et dolore magna aliqua. Ut enim ad minim veniam, quis nostrud exercitation ut.</p>
  <span class="more">Learn More <svg width="22" height="6"><path d="M0 3h20M16 0l4 3-4 3" fill="none" stroke="#6f4fbd"/></svg></span>
</div>
<div class="abs blog-card" style="left:763px">
  <div class="img" role="img" aria-label="Photo of a woodworker gluing a carved panel in a workshop" style="background:linear-gradient(135deg,#8a8079,#3b3f52 50%,#a0613a)"></div>
  <h3>Use glue in woodwork like this</h3>
  <p>Lorem ipsum dolor sit amet, consectetur adipisicing elit, sed do eiusmod tempor incididunt ut labore et dolore magna aliqua. Ut enim ad minim veniam, quis nostrud exercitation ut.</p>
  <span class="more">Learn More <svg width="22" height="6"><path d="M0 3h20M16 0l4 3-4 3" fill="none" stroke="#6f4fbd"/></svg></span>
</div>
<a class="abs btn btn-white" style="left:506px;top:2409px;width:188px;height:37px;line-height:37px">View All Blog Posts</a>

<div class="abs footer"></div>
<div class="abs f-logo">Logo</div>
<div class="abs f-head" style="left:149px">Glue</div>
<div class="abs f-select" style="top:2649px">Select <svg width="12" height="7"><path d="M1 1l5 5 5-5" fill="none" stroke="#2f2a4e" stroke-width="1.2"/></svg></div>
<div class="abs" style="left:210px;top:2680px;font-size:14px;font-weight:500">to</div>
<div class="abs f-select" style="top:2699px">Select <svg width="12" height="7"><path d="M1 1l5 5 5-5" fill="none" stroke="#2f2a4e" stroke-width="1.2"/></svg></div>
<a class="abs btn btn-purple" style="left:149px;top:2749px;width:137px;height:30px;line-height:30px;font-weight:500">Compare</a>

<div class="abs f-head" style="left:366px">Products</div>
<ul class="abs f-list" style="left:367px"><li>Wood and paper</li><li>Rubber and wood</li><li>Fabric and leather</li><li>Leather and metal</li><li>Metal and wood</li><li><i>More</i></li></ul>
<div class="abs f-head" style="left:561px;top:2612px">Home</div>
<ul class="abs f-list" style="left:562px"><li>Category</li><li>Products</li><li>About Us</li><li>Terms &amp; Conditions</li></ul>
<div class="abs f-head" style="left:761px">Blog Posts</div>
<ul class="abs f-list" style="left:762px"><li>Article 1</li><li>Article 2</li><li>Article 3</li></ul>
<div class="abs f-head" style="left:945px">Let's Connect</div>
<ul class="abs f-list" style="left:946px"><li>(555) 014-2290</li><li>P.O. Box 40872</li><li>Fairview, ST 10482</li><li>Email Us</li></ul>

<div class="abs f-line"></div>
<div class="abs social"><i></i><i></i><i></i><i></i></div>
<div class="abs legal" style="left:855px">© 2020 Logo Inc</div>
<div class="abs legal" style="left:937px">Legal</div>
<div class="abs legal" style="left:977px">Privacy</div>
<div class="abs legal" style="left:1027px">Brand</div>

</body>
</html>
```